Business Card for Professional Photographer

I'm looking for an eye catching modern clean design that compliments my logo/ website fonts & colours.
I specialise in architecture, corporate & commercial photography so I'm marketing to professional clients rather than portrait / wedding clients.

I would prefer to not have a solid black design.

My logo brand guide is as follows :

Main front font. : Reislust
Main font colour : #fff
Slogan front font : Ubuntu Bold
Monogram front font : Venti Medium
Container colour : #fff

I need print ready files in pdf .png & .eps formats.

Included in the files below are some screen grabs as reference to font & colours etc.

```html
<!DOCTYPE html>
<html lang="en">
<head>
<meta charset="utf-8">
<title>Clearline Studio – Business Card</title>
<link href="https://fonts.googleapis.com/css2?family=Lato:wght@400&family=Montserrat:wght@400;500;700&family=Ubuntu:wght@700&display=swap" rel="stylesheet">
<style>
  :root {
    --backdrop: #1d1d1f;
    --card: #eff1f4;
    --gold: #b9893f;
    --gold-light: #e6c67a;
    --grey-title: #8a8a8d;
    --grey-text: #555558;
  }
  * { box-sizing: border-box; margin: 0; padding: 0; }
  html, body { width: 1200px; height: 900px; overflow: hidden; }
  body { background: var(--backdrop); position: relative; }

  .card { position: absolute; }
  .card-shape { position: absolute; inset: 0; width: 100%; height: 100%; }
  .card-shape path { fill: var(--card); }
  .card--front { left: 132px; top: 225px; width: 453px; height: 382px; }
  .card--back  { left: 628px; top: 232px; width: 437px; height: 368px; }

  .brand {
    position: absolute; left: 0; right: 0;
    display: flex; align-items: center; justify-content: center; gap: 12px;
  }
  .brand-dot { border-radius: 50%; background: var(--gold); flex: none; }
  .brand-name {
    font-family: "Montserrat", sans-serif; font-weight: 400;
    color: var(--gold); text-transform: uppercase; white-space: nowrap;
  }
  .brand-tagline {
    font-family: "Ubuntu", sans-serif; font-weight: 700; color: var(--gold);
    text-transform: capitalize; white-space: nowrap; margin-top: 4px;
  }
  .card--front .brand { top: 80px; }
  .card--front .brand-dot { width: 22px; height: 22px; }
  .card--front .brand-name { font-size: 15px; letter-spacing: 3.4px; }
  .card--front .brand-tagline { font-size: 6px; letter-spacing: 2px; }
  .card--back .brand { top: 182px; gap: 16px; }
  .card--back .brand-dot { width: 28px; height: 28px; }
  .card--back .brand-name { font-size: 19px; letter-spacing: 4.2px; }
  .card--back .brand-tagline { font-size: 7px; letter-spacing: 2.6px; }

  .contact-block {
    position: absolute; left: 0; right: 0; top: 176px; text-align: center;
  }
  .person-name {
    font-family: "Montserrat", sans-serif; font-weight: 700;
    font-size: 18px; color: var(--gold); letter-spacing: 0.2px;
  }
  .person-role {
    font-family: "Montserrat", sans-serif; font-weight: 500;
    font-size: 15px; color: var(--grey-title); margin-top: 4px;
  }
  .divider { width: 18px; height: 2px; background: var(--gold); margin: 10px auto 0; }
  .icon-row { display: flex; justify-content: center; gap: 5px; margin-top: 12px; }
  .icon-badge {
    width: 18px; height: 18px; border-radius: 50%;
    background: linear-gradient(135deg, var(--gold), var(--gold-light));
    display: flex; align-items: center; justify-content: center;
  }
  .icon-badge svg { width: 10px; height: 10px; }
  .contact-lines { margin-top: 9px; }
  .contact-line {
    font-family: "Lato", sans-serif; font-weight: 400;
    font-size: 15.5px; color: var(--grey-text); line-height: 25px;
  }
</style>
</head>
<body>

  <section class="card card--front">
    <svg class="card-shape" viewBox="0 0 453 382" aria-hidden="true">
      <path d="M0,113 Q0,53 60,53 L97,53 Q105,0 165,0 L287,0 Q347,0 355,53 L393,53 Q453,53 453,113 L453,322 Q453,382 393,382 L60,382 Q0,382 0,322 Z"/>
    </svg>
    <div class="brand">
      <span class="brand-dot"></span>
      <div>
        <div class="brand-name">Clearline Studio</div>
        <div class="brand-tagline">Architecture Corporate Commercial</div>
      </div>
    </div>
    <div class="contact-block">
      <p class="person-name">RENATA VALLIS</p>
      <p class="person-role">Manager</p>
      <div class="divider"></div>
      <div class="icon-row">
        <span class="icon-badge"><svg viewBox="0 0 10 10"><path d="M2 1 L3.6 1 L4.2 3 L3.2 3.8 Q4 5.8 6.2 6.8 L7 5.8 L9 6.4 L9 8 Q8.6 9 7.6 9 Q2.6 8.4 1 2.4 Q1 1.4 2 1 Z" fill="#fff"/></svg></span>
        <span class="icon-badge"><svg viewBox="0 0 10 10"><rect x="1" y="2.2" width="8" height="5.6" fill="none" stroke="#fff" stroke-width="1"/><path d="M1 2.4 L5 5.6 L9 2.4" fill="none" stroke="#fff" stroke-width="1"/></svg></span>
        <span class="icon-badge"><svg viewBox="0 0 10 10"><circle cx="5" cy="5" r="3.8" fill="none" stroke="#fff" stroke-width="1"/><ellipse cx="5" cy="5" rx="1.6" ry="3.8" fill="none" stroke="#fff" stroke-width="0.8"/><path d="M1.2 5 H8.8" stroke="#fff" stroke-width="0.8"/></svg></span>
      </div>
      <div class="contact-lines">
        <p class="contact-line">613-555-0142</p>
        <p class="contact-line">info@clearlinestudio.com</p>
        <p class="contact-line">www.clearlinestudio.com</p>
      </div>
    </div>
  </section>

  <section class="card card--back">
    <svg class="card-shape" viewBox="0 0 437 368" aria-hidden="true">
      <path d="M0,108 Q0,51 58,51 L94,51 Q102,0 160,0 L275,0 Q333,0 342,51 L379,51 Q437,51 437,108 L437,310 Q437,368 379,368 L58,368 Q0,368 0,310 Z"/>
    </svg>
    <div class="brand">
      <span class="brand-dot"></span>
      <div>
        <div class="brand-name">Clearline Studio</div>
        <div class="brand-tagline">Architecture Corporate Commercial</div>
      </div>
    </div>
  </section>

</body>
</html>
```